Postcard: Open Sky Circle

Text for front: HOW TO CHANGE THE WORLD IN ONE [note: the word "one" should be underlined] STEPHint: It's up to you...[Note: add arrow or something to indicate "turn over"]Text for back: You're going to spend your entire life with someone you can never get away from. (Guess who?) Wouldn't you rather that person #OpenSkyCircle than judgmental or critical? BE the change you want to see! Visit www.OpenSkyCircle-hub.example for daily Dawn Pebbles and community. PLEASE JOIN US![Note: add logo to left half of back side]Font preference for text: Josefin sans

Target Market(s)

People who would be attracted to Corvane church - teravian perennist message. It's spiritual without being overtly religious, so the target market is probably early 30s and up but ideally won't turn off Millennials (folks under 30). It should attract attention of people who are open-minded and committed to progressive social change, tired of an atmosphere of hate-mongering and divisiveness.

Requirements
Nice to have
• It would be nice to convey a sense of challenge - there is an idea of "dawn pebbles" so something related to fire/sparks is appropriate. This is meant to evoke a deeper, divine love more than a sense of romantic love. This love is more fierce than fluffy! Yet it calls us to be our best selves.
Should not have
• Please avoid excessive pink - just the logo is enough, as this design needs to appeal to men as well as women.

```html
<!DOCTYPE html>
<html lang="en">
<head>
<meta charset="utf-8">
<title>Open Sky Circle – Postcard</title>
<link href="https://fonts.googleapis.com/css2?family=Josefin+Sans:ital,wght@0,400;0,600;0,700;1,400&family=Amatic+SC:wght@700&display=swap" rel="stylesheet">
<style>
  :root{
    --board:#cbcbcb;
    --sea:#0fab9e;
    --sea-deep:#1a8a98;
    --teal:#13808e;
    --teal-dark:#0d6b78;
    --leaf:#a5d24a;
    --leaf-dark:#7fb233;
    --ink:#2b2b2b;
    --label:#3a3a3a;
    --white:#ffffff;
  }
  *{margin:0;padding:0;box-sizing:border-box}
  html,body{width:960px;height:1200px;overflow:hidden;background:var(--board)}
  body{position:relative;font-family:"Josefin Sans",sans-serif}
  .card{position:absolute;left:107px;width:746px;overflow:hidden;box-shadow:0 6px 14px rgba(0,0,0,.28)}
  .card--front{top:42px;height:498px;background:var(--sea)}
  .card--back{top:618px;height:496px;background:var(--white)}
  .page-label{position:absolute;left:0;width:960px;text-align:center;font-weight:700;font-size:29px;letter-spacing:3px;color:var(--label)}
  .page-label--front{top:555px}
  .page-label--back{top:1129px}
  .card-art{position:absolute;inset:0}
  .ribbon-kicker{position:absolute;left:150px;top:185px;width:330px;text-align:center;color:var(--white);font-weight:600;font-size:17px;letter-spacing:1.5px;transform:rotate(-8deg)}
  .ribbon-title{position:absolute;left:160px;top:210px;width:320px;text-align:center;color:var(--white);font-family:"Amatic SC",cursive;font-size:96px;line-height:1;transform:rotate(-7deg)}
  .ribbon-title .one{text-decoration:underline;text-decoration-thickness:3px;text-underline-offset:6px}
  .hint{position:absolute;left:560px;top:340px;width:180px;text-align:center;transform:rotate(-6deg)}
  .hint-label{font-family:"Amatic SC",cursive;font-size:36px;color:var(--white);line-height:1}
  .hint-text{font-size:27px;color:var(--leaf);font-weight:600;line-height:1.1}
  .logo-name{position:absolute;left:30px;top:170px;width:300px;text-align:center;font-weight:700;font-size:46px;line-height:1.05;color:var(--leaf)}
  .message{position:absolute;left:366px;top:36px;width:360px;text-align:center;font-size:19px;line-height:25px;color:var(--ink)}
  .accent{color:var(--leaf-dark)}
  .visit{position:absolute;left:380px;top:250px;width:360px;text-align:center;transform:rotate(-3deg)}
  .visit-label{font-family:"Amatic SC",cursive;font-size:38px;color:var(--white);line-height:1}
  .visit-url{font-size:20px;font-weight:600;color:var(--leaf);margin-top:6px}
  .tagline{position:absolute;left:366px;top:356px;width:360px;text-align:center;font-size:19px;color:var(--ink)}
  .footer-rule{position:absolute;left:0;top:403px;width:746px;height:5px;background:var(--leaf)}
  .footer-band{position:absolute;left:0;top:408px;width:746px;height:88px;background:linear-gradient(var(--teal),var(--teal-dark));color:var(--white);font-weight:600;font-size:40px;letter-spacing:2px;text-align:center;line-height:94px}
</style>
</head>
<body>

<section class="card card--front">
  <svg class="card-art" width="746" height="498" viewBox="0 0 746 498">
    <defs>
      <radialGradient id="glow" cx="321" cy="222" r="300" gradientUnits="userSpaceOnUse">
        <stop offset="0.6" stop-color="#6fd2c9" stop-opacity=".55"/>
        <stop offset="1" stop-color="#0fab9e" stop-opacity="0"/>
      </radialGradient>
      <linearGradient id="ribbonFill" x1="0" y1="0" x2="1" y2="0">
        <stop offset="0" stop-color="#8fc23c"/>
        <stop offset=".5" stop-color="#a9d54e"/>
        <stop offset="1" stop-color="#8fc23c"/>
      </linearGradient>
    </defs>
    <circle cx="321" cy="222" r="300" fill="url(#glow)" role="img" aria-label="Radiating sunburst rays behind the globe"/>
    <circle cx="321" cy="222" r="204" fill="var(--sea-deep)" role="img" aria-label="Globe illustration with green continents"/>
    <path d="M41,262 Q200,195 501,150 L573,106 Q600,170 609,238 Q560,250 509,274 Q380,290 253,302 Q150,320 89,374 Q55,320 41,262 Z" fill="url(#ribbonFill)"/>
    <path d="M529,330 Q640,318 746,298 L746,420 Q650,440 530,442 Q548,390 529,330 Z" fill="var(--teal)"/>
    <path d="M640,440 Q680,462 712,458" fill="none" stroke="var(--leaf)" stroke-width="9" stroke-linecap="round"/>
    <path d="M700,444 L726,457 L704,474 Z" fill="var(--leaf)"/>
  </svg>
  <p class="ribbon-kicker">HOW TO CHANGE THE WORLD IN</p>
  <h1 class="ribbon-title"><span class="one">ONE</span> STEP</h1>
  <div class="hint">
    <p class="hint-label">HINT:</p>
    <p class="hint-text">It’s up to you</p>
  </div>
</section>
<p class="page-label page-label--front">FRONT PAGE</p>

<section class="card card--back">
  <p class="logo-name">Open Sky<br>Circle</p>
  <p class="message">You're going to spend your entire life with someone you can never get away from. <span class="accent"><i>(Guess who?)</i></span><br>Wouldn't you rather that person <span class="accent">#OpenSkyCircle</span> than judgmental or critical? BE the change you want to see!</p>
  <svg class="card-art" width="746" height="496" viewBox="0 0 746 496">
    <path d="M386,206 Q560,240 746,210 L746,300 Q600,340 364,334 Q380,270 386,206 Z" fill="var(--teal)"/>
  </svg>
  <div class="visit">
    <p class="visit-label">VISIT:</p>
    <p class="visit-url">www.OpenSkyCircle-hub.example</p>
  </div>
  <p class="tagline">for daily Dawn Pebbles and community.</p>
  <div class="footer-rule"></div>
  <p class="footer-band">PLEASE JOIN US!</p>
</section>
<p class="page-label page-label--back">BACK PAGE</p>

</body>
</html>
```